Wordpress Theme Design for Family Law Firm

Hello, this is a WordPress theme design project, for a "Divorce and Family Law Mediation" practice.

I'd want the wordpress theme to be modeled loosely on this existing design from another one of our own sites: http://www.corvel-debtrelief-guide.example/

We want it to be bright and vibrant and convey a happy and relaxed feeling. The lines on it to not be sharp so more of the rounded edges and subtle shadows that you see on the example site.

Although built on WordPress, the site will be mostly static with fixed content pages, but including a blog feature.

The images will need to be different, but conveying a similar look and feel as the sample site. The colors from the sample site are close to what I'd like - but open to creative options.

It's important that the site looks professional, as well as friendly, and conveys the idea of mediation and relationships.

Important note: Traditional divorce website is for people looking to fight or being bullied.

Divorce mediation is for couples who have decided to split amicably so they're in a much more cooperative state of mind. There's not as much stress and anger. It's just about HOW we go about finalizing the process. There's light at the end of the tunnel.

With that in mind, the site should look friendly and happy, with an inspiring theme of a bright future.

Target Market(s)

The target market are people looking for amicable resolution, with a happy and uplifting attitude..

Traditional divorce websites are for people generally looking to fight or being bullied.

Divorce mediation (this website) is for couples who have decided to split amicably so they're in a much more cooperative state of mind. There's not as much stress and anger. It's just about HOW we go about finalizing the process. There's light at the end of the tunnel.

Industry/Entity Type

Family Law

Requirements
Must have
• Must have option for 1 or two sidebars for pages. This is because some of the internal pages will only have a single sidebar.

The footer will have the option for widgets.

```html
<!DOCTYPE html>
<html lang="en">
<head>
<meta charset="utf-8">
<title>Meridian Law Group</title>
<link href="https://fonts.googleapis.com/css2?family=Arimo:wght@400;700&family=Roboto+Condensed:wght@400;500&display=swap" rel="stylesheet">
<style>
:root{
  --navy:#1f4a7f;
  --navy-dark:#1a3f6e;
  --blue:#3d73ae;
  --sky:#cfe3f6;
  --heading:#1d4b82;
  --text:#555;
  --nav-text:#14325a;
  --line:#c9cfd6;
  --white:#fff;
}
*{margin:0;padding:0;box-sizing:border-box}
html,body{width:1200px;height:974px;overflow:hidden}
body{position:relative;background:linear-gradient(#234f86 0,#5d86b6 45px,#c7d6e8 90px,#fff 135px,#fff);font-family:Arimo,Arial,sans-serif;color:var(--text)}
.abs{position:absolute}

.brand{left:115px;top:30px;width:210px;height:72px;background:linear-gradient(#fff,#eef1f4);border-radius:8px 8px 0 0;border:1px solid #d7dde4;border-bottom:none;box-shadow:0 -1px 4px rgba(0,0,0,.2);display:flex;align-items:center;padding-left:14px;gap:10px}
.brand-mark{width:30px;height:30px;border-radius:50%;background:#6fa6d8}
.brand-name{font-family:Arimo,Arial,sans-serif;font-size:19px;color:#2a5a8c;line-height:1.1;letter-spacing:1px}

.callbar{left:677px;top:64px;width:412px;height:37px;background:linear-gradient(#8fa9cf,#5a80b6);border-radius:8px 8px 0 0;color:#fff;display:flex;align-items:center;padding-left:22px;font-size:11px;text-shadow:0 1px 1px rgba(0,0,0,.35)}
.callbar strong{font-size:17px;font-weight:400;margin-left:8px}

.nav{left:110px;top:101px;width:979px;height:33px;background:linear-gradient(#fff,#eceef0);border:1px solid #d8dce0;border-radius:4px;box-shadow:0 2px 4px rgba(0,0,0,.12);display:flex;align-items:center;font-size:11px;color:var(--nav-text)}
.nav a{color:inherit;text-decoration:none;padding:0 26px;border-right:1px solid var(--line);line-height:18px}
.nav a:last-child{border:none}

.hero{left:110px;top:150px;width:724px;height:211px;border-radius:4px;overflow:hidden;background:linear-gradient(90deg,#3b6aa0,#7d9fc6 55%,#5a83b6)}
.hero-photo{left:0;top:0;width:330px;height:211px;background:linear-gradient(90deg,#2f5b8f,#8a9fb5 55%,#4d77a9)}
.hero h1{left:321px;top:46px;font-family:Arimo,Arial,sans-serif;font-weight:400;font-size:31px;line-height:32px;color:#fff;letter-spacing:-.5px;width:400px}
.hero p{left:325px;top:118px;font-size:14px;color:#fff}
.hero .btn{left:326px;top:148px;width:192px;height:36px;border-radius:6px;background:linear-gradient(#3bb0ee,#0b7bc9);color:#fff;font-size:15px;display:flex;align-items:center;justify-content:center;box-shadow:0 2px 3px rgba(0,0,0,.3)}
.dots{left:646px;top:186px;display:flex;gap:3px}
.dots i{width:10px;height:10px;border-radius:2px;background:#d5e0ec}
.dots i:first-child{background:#5aaee8}

.help{left:850px;top:150px;width:239px;height:129px;border:1px solid #b9d2ea;border-radius:4px;background:linear-gradient(#bedbf4,#fff);overflow:hidden}
.help h2{left:17px;top:11px;font-family:"Roboto Condensed",sans-serif;font-weight:400;font-size:19px;line-height:22px;color:#3e5d8a}
.help p{left:15px;top:57px;width:106px;font-size:11px;line-height:16px;color:#444}
.help-photo{right:0;top:4px;width:118px;height:125px;background:linear-gradient(#bcd3ea,#2a3342)}
.promo{left:849px;top:288px;width:241px;height:73px;border:1px solid #cfd5dc;border-radius:4px;background:#fff}
.promo-art{left:8px;top:5px;width:80px;height:62px;background:linear-gradient(#dfe3e8,#a7afb8);border-radius:4px}
.promo h3{left:97px;top:11px;font-weight:400;font-size:13px;line-height:16px;color:#1d4a83}
.promo p{left:98px;top:45px;font-size:11px;color:#444}

.services{left:110px;top:376px;width:979px;height:247px;background:linear-gradient(var(--navy-dark),#4e86c3);border-radius:5px}
.card{top:10px;width:233px;height:229px;border-radius:5px;background:linear-gradient(#5586bd 0,#aecbe6 95px,#fff 135px);text-align:center}
.card h4{font-family:"Roboto Condensed",sans-serif;font-weight:400;color:#fff;font-size:27px;line-height:24px;margin-top:38px;text-shadow:0 1px 2px rgba(0,0,0,.25)}
.card h4 small{display:block;font-size:20px;line-height:18px}
.card p{font-size:11px;line-height:18px;color:#111;margin:9px 12px 0}
.card .art{position:absolute;left:50%;transform:translateX(-50%);bottom:30px;width:72px;height:62px;border-radius:10px}

.intro h2{left:111px;top:646px;font-family:"Roboto Condensed",sans-serif;font-weight:500;font-size:20px;line-height:23px;color:var(--heading);width:600px}
.intro p{left:110px;width:724px;font-size:11px;line-height:18px;color:#555;text-align:justify}

.contact h2{left:862px;top:645px;font-family:"Roboto Condensed",sans-serif;font-weight:500;font-size:20px;color:var(--heading)}
.contact .sub{left:863px;top:673px;font-size:13px;color:#111}
.field-label{width:60px;text-align:right;font-size:11px;color:var(--nav-text)}
.field{left:928px;width:163px;height:21px;border:1px solid #c7ccd2;border-radius:4px;background:linear-gradient(#f4f5f6,#fff)}
.send{left:1035px;top:840px;width:55px;height:20px;border-radius:3px;background:linear-gradient(#5a83b8,#1d4a82);color:#fff;font-size:10px;display:flex;align-items:center;justify-content:center}

.footer{left:110px;top:875px;width:979px;height:75px;background:linear-gradient(#e2e4e6,#fff);border-radius:5px 5px 0 0}
.badges{left:10px;top:8px;width:145px;height:66px;background:linear-gradient(#fff,#e3e5e8);border-radius:4px;box-shadow:0 1px 3px rgba(0,0,0,.25)}
.badge-round{left:12px;top:7px;width:62px;height:50px;border-radius:50%;background:#3b8fd0}
.badge-square{left:85px;top:8px;width:50px;height:50px;border-radius:6px;background:#2b5f9b}
.foot-nav{left:175px;top:21px;font-size:11px;color:#444;display:flex}
.foot-nav span{padding:0 14px;border-left:1px solid #777;line-height:12px}
.foot-nav span:first-child{padding-left:0;border:none}
.copy{left:176px;top:42px;font-size:10px;color:#1d3d6a}
.follow{left:801px;top:14px;width:169px;height:32px;border:1px solid #cdd2d8;border-radius:5px;background:#fff;display:flex;align-items:center;padding-left:15px;gap:4px;font-family:"Roboto Condensed",sans-serif;font-size:14px;color:#555}
.follow i{width:20px;height:20px;border-radius:50%;background:#3a78b8;margin-left:1px}
.follow i:first-of-type{margin-left:6px}
</style>
</head>
<body>

<div class="abs brand"><span class="brand-mark"></span><span class="brand-name">MERIDIAN<br>LAW GROUP</span></div>
<div class="abs callbar">CALL TODAY FOR A FREE PHONE CONSULTATION : <strong>0000 000 000</strong></div>

<nav class="abs nav">
  <a href="#">HOME</a><a href="#">FIRM OVERVIEW</a><a href="#">ABOUT US</a><a href="#">SERVICES</a><a href="#">FAQ</a><a href="#">TESTIMONIALS</a><a href="#">BLOG</a><a href="#">CONTACT US</a>
</nav>

<section class="abs hero">
  <div class="abs hero-photo" role="img" aria-label="Photo of a smiling professional woman in a business jacket"></div>
  <h1 class="abs">Lorem Ipsum is simply dummy text of the printing</h1>
  <p class="abs">Lorem Ipsum is simply dummy text of the printing</p>
  <div class="abs btn">Click Here to Readmore</div>
  <div class="abs dots"><i></i><i></i><i></i><i></i><i></i></div>
</section>

<aside class="abs help">
  <h2 class="abs">HOW CAN WE<br>HELP ?</h2>
  <p class="abs">Lorem Ipsum is simply dummy text of the printing and typesetting industry.</p>
  <div class="abs help-photo" role="img" aria-label="Photo of a friendly lawyer in a suit"></div>
</aside>
<aside class="abs promo">
  <div class="abs promo-art" role="img" aria-label="Illustration of a courthouse with a green tick"></div>
  <h3 class="abs">Lorem Ipsum is simply<br>of the dummy</h3>
  <p class="abs">Lorem Ipsum is thesimply</p>
</aside>

<section class="abs services">
  <div class="abs card" style="left:10px"><h4>DIVORCE</h4><p>Lorem Ipsum is simply dummy text of the printing and typesetting industry. Lorem Ipsum.</p><div class="art" role="img" aria-label="Illustration of a broken heart" style="background:#c8242a;bottom:28px;width:74px;height:58px"></div></div>
  <div class="abs card" style="left:253px"><h4>FAMILY<small>LAW MEDIATION</small></h4><p>Lorem Ipsum is simply dummy text of the printing and typesetting.</p><div class="art" role="img" aria-label="Illustration of a family of three" style="background:linear-gradient(90deg,#4a4a4a,#d63c9a)"></div></div>
  <div class="abs card" style="left:496px"><h4>FIRM<small>OVERVIEW</small></h4><p>Lorem Ipsum is simply dummy text of the printing and typesetting..</p><div class="art" role="img" aria-label="Illustration of golden scales of justice" style="background:#b7853a;bottom:24px;height:72px"></div></div>
  <div class="abs card" style="left:739px"><h4>LOREM IPSUM<small>IS SIMPLY</small></h4><p>Lorem Ipsum is simply dummy text of the printing and typesetting.</p><div class="art" role="img" aria-label="Illustration of a wooden gavel" style="background:#7a4a26;width:64px"></div></div>
</section>

<section class="intro">
  <h2 class="abs">LOREM IPSUM IS SIMPLY DUMMY<br>TEXT OF THE PRINTING AND TYPESETTING INDUSTRY.</h2>
  <p class="abs" style="top:699px">Lorem Ipsum is simply dummy text of the printing and typesetting industry. Lorem Ipsum has been the industry's standard dummy text ever since the 1500s, when an unknown printer took a galley of type and scrambled it to make a type specimen book. It has survived not only five centuries, but also the leap into electronic typesetting, remaining essentially unchanged. It was popularised in the 1960s with the release of Letraset sheets containing Lorem Ipsum passages, and more recently with desktop publishing software like Aldus PageMaker including versions of Lorem Ipsum.</p>
  <p class="abs" style="top:789px">Lorem Ipsum is simply dummy text of the printing and typesetting industry. Lorem Ipsum has been the industry's standard dummy text ever since the 1500s, when an unknown printer took a galley of type and scrambled it to make a type specimen book. It has survived not only five centuries, but also the leap into electronic typesetting, remaining essentially unchanged.</p>
</section>

<section class="contact">
  <h2 class="abs">CONTACT FORM</h2>
  <div class="abs sub">EMAIL US WITH YOUR QUESTIONS</div>
  <div class="abs field-label" style="left:861px;top:703px">Name :</div><div class="abs field" style="top:699px"></div>
  <div class="abs field-label" style="left:861px;top:733px">Email :</div><div class="abs field" style="top:729px"></div>
  <div class="abs field-label" style="left:861px;top:763px">Phone :</div><div class="abs field" style="top:759px"></div>
  <div class="abs field-label" style="left:861px;top:793px">Message :</div><div class="abs field" style="top:789px;height:41px"></div>
  <div class="abs send">SEND</div>
</section>

<footer class="abs footer">
  <div class="abs badges"><div class="abs badge-round"></div><div class="abs badge-square"></div></div>
  <div class="abs foot-nav"><span>Home</span><span>Firm Overview</span><span>About Us</span><span>Services</span><span>Faq</span><span>Testimonials</span><span>Blog</span><span>Contact Us</span></div>
  <div class="abs copy">© 2012. Meridian Law Group. All Rights Reserved.</div>
  <div class="abs follow">Follow Us :<i></i><i></i><i></i></div>
</footer>

</body>
</html>
```